Magazine advertisement

I need a company advertisement for magazine prints. I need to be able to scale it to different sizes if need be. I need it to showcase our brand, VornaDrive have our phone number 582.463.9047 our contact email address sales@vornadrive.net and web address www.vornadrive.net

Target Market(s)

automotive / tractor pulling

Industry/Entity Type

automotive / racing

Colors
EB3D1F
EC4F4E
F09395
F8D3D4
FCEDEE

Requirements
Must have
• our logo, our color scheme (pantone red 1795, white, black, silver

```html
<!DOCTYPE html>
<html lang="en">
<head>
<meta charset="UTF-8">
<title>VornaDrive – Custom Turbochargers</title>
<link href="https://fonts.googleapis.com/css2?family=Poppins:ital,wght@0,400;0,500;0,600;0,700;0,800;1,700&display=swap" rel="stylesheet">
<style>
  :root{
    --red:#e0262b;
    --red-bright:#eb3d1f;
    --black:#1c1c1e;
    --ink:#2a2a2a;
    --body:#444;
    --paper:#f1f1f1;
    --paper-edge:#e3e3e3;
    --silver-light:#f4f4f4;
    --silver:#c4c4c6;
    --silver-dark:#8a8a8e;
    --stage:#d6d6d6;
  }
  *{margin:0;padding:0;box-sizing:border-box}
  html,body{width:675px;height:1200px;overflow:hidden}
  body{background:var(--stage);font-family:'Poppins',sans-serif;display:flex;align-items:center;justify-content:center}
  .ad{position:relative;width:600px;height:776px;background:linear-gradient(160deg,#fafafa 0%,var(--paper) 45%,var(--paper-edge) 100%);overflow:hidden;box-shadow:0 6px 24px rgba(0,0,0,.25)}
  .abs{position:absolute}
  .web-band{left:363px;top:35px;width:237px;height:26px;background:var(--red);clip-path:polygon(6% 0,100% 0,100% 100%,0 100%);color:#fff;font-size:11px;font-weight:600;display:flex;align-items:center;justify-content:center;letter-spacing:.3px}
  .brand{left:45px;top:72px;display:flex;align-items:center;gap:10px;font-size:30px;font-weight:800;color:var(--red);letter-spacing:.5px}
  .brand-mark{width:16px;height:16px;background:var(--black)}
  .tag-custom{left:39px;top:137px;width:206px;height:41px;background:var(--red);clip-path:polygon(0 0,94% 0,100% 100%,0 100%);color:#fff;font-size:27px;font-weight:700;padding-left:22px;line-height:41px}
  .tag-turbo{left:37px;top:183px;width:308px;height:45px;background:var(--black);clip-path:polygon(4% 0,100% 0,100% 100%,0 100%);color:#fff;font-size:30px;font-weight:700;padding-left:26px;line-height:45px}
  .subhead{left:66px;top:238px;font-size:17px;font-weight:700;font-style:italic;color:var(--ink)}
  .hero-photo{left:340px;top:83px;width:217px;height:233px;border-radius:50%;background:radial-gradient(circle at 45% 45%,var(--silver-light) 0%,var(--silver) 45%,var(--silver-dark) 85%,transparent 100%)}
  .feature h3{font-size:13px;font-weight:700;color:var(--ink);display:flex;align-items:center;gap:6px}
  .feature h3::before{content:"";width:3px;height:11px;background:var(--red);transform:skewX(-20deg)}
  .feature h3 span{color:var(--red)}
  .feature p{margin:4px 0 0 18px;font-size:10px;line-height:13px;color:var(--body);width:210px}
  .f-turbine{left:45px;top:302px}
  .f-win{left:45px;top:393px}
  .f-about{left:320px;top:393px}
  .peak{left:423px;top:334px;width:58px;height:19px;background:var(--red);clip-path:polygon(8% 0,100% 0,92% 100%,0 100%);color:#fff;font-size:12px;font-weight:700;font-style:italic;text-align:center;line-height:19px}
  .performance{left:415px;top:354px;width:136px;height:24px;background:var(--black);clip-path:polygon(5% 0,100% 0,95% 100%,0 100%);color:#fff;font-size:13px;font-weight:700;font-style:italic;text-align:center;line-height:24px}
  .featured-band{left:188px;top:494px;width:228px;height:30px;background:var(--red);clip-path:polygon(4% 0,100% 0,96% 100%,0 100%);color:#fff;font-size:15px;font-weight:600;text-align:center;line-height:30px}
  .product{top:545px;width:150px}
  .product .photo{width:130px;height:118px;border-radius:50%;background:radial-gradient(circle at 50% 50%,var(--silver-light) 0%,var(--silver) 50%,var(--silver-dark) 85%,transparent 100%);margin-left:0}
  .product .name{margin-top:8px;font-size:11px;font-weight:700;color:var(--red)}
  .product .spec{font-size:9px;color:var(--body)}
  .p1{left:45px}.p2{left:215px}.p3{left:380px}
  .footer{left:0;top:717px;width:600px;height:59px;background:var(--black);display:flex;align-items:center;padding-left:42px;gap:12px;color:#fff;font-size:11px}
  .footer .item{display:flex;align-items:center;gap:5px}
  .footer .sep{color:#888}
  .footer svg{width:10px;height:10px;fill:var(--red)}
</style>
</head>
<body>
<div class="ad">
  <div class="abs web-band">www.vornadrive.net</div>
  <div class="abs brand"><span class="brand-mark"></span>VornaDrive</div>

  <div class="abs tag-custom">Custom</div>
  <div class="abs tag-turbo">Turbochargers</div>
  <div class="abs subhead">for Extreme Motorsports</div>
  <div class="abs hero-photo" role="img" aria-label="Photo of a polished silver billet turbocharger"></div>

  <div class="abs feature f-turbine">
    <h3>One Fierce <span>Turbine</span></h3>
    <p>Our hub-free design maximizes aerodynamics and has been dyno-proven to yield maximum horsepower without the need to increase frame size.</p>
  </div>
  <div class="abs peak">Peak</div>
  <div class="abs performance">Performance</div>
  <div class="abs feature f-win">
    <h3>Built to <span>Win</span></h3>
    <p>We'll help you perform like a winner, from truck and tractor pulling to drag racing. Our turbochargers are equipped with the capacity to power everything from high-end sports cars to snowmobiles.</p>
  </div>
  <div class="abs feature f-about">
    <h3>About <span>VornaDrive</span></h3>
    <p>Revolutionizing the drag car, truck, tractor and sled-pulling industry, the team at VornaDrive continues to out perform the competition when it comes to high-performance turbochargers.</p>
  </div>

  <div class="abs featured-band">Featured Turbos</div>
  <div class="abs product p1">
    <div class="photo" role="img" aria-label="Photo of the VDX 4.8 SL turbocharger"></div>
    <div class="name">VDX 4.8 SL</div>
    <div class="spec">4.8" Compressor | 4.65" Turbine</div>
  </div>
  <div class="abs product p2">
    <div class="photo" role="img" aria-label="Photo of the VDX 3.4X4 SB turbocharger"></div>
    <div class="name">VDX 3.4X4 SB</div>
    <div class="spec">3.4" Compressor | 4.0" Turbine</div>
  </div>
  <div class="abs product p3">
    <div class="photo" role="img" aria-label="Photo of the VDX 3X4 SL turbocharger"></div>
    <div class="name">VDX 3X4 SL</div>
    <div class="spec">3.0" Compressor | 4.0" Turbine</div>
  </div>

  <div class="abs footer">
    <span class="item"><svg viewBox="0 0 10 10"><path d="M5 0a3.5 3.5 0 0 0-3.5 3.5C1.5 6 5 10 5 10s3.5-4 3.5-6.5A3.5 3.5 0 0 0 5 0zm0 5a1.5 1.5 0 1 1 0-3 1.5 1.5 0 0 1 0 3z"/></svg>Alder Falls, MI 49012</span>
    <span class="sep">|</span>
    <span class="item"><svg viewBox="0 0 10 10"><path d="M2 0l2 2.5-1 1.2a6 6 0 0 0 3.3 3.3l1.2-1L10 8l-1.2 1.6C4.5 10 0 5.5.4 1.2z"/></svg>582.463.9047</span>
    <span class="sep">|</span>
    <span class="item"><svg viewBox="0 0 10 10"><path d="M0 2h10v6H0zm1 .8v.4l4 2.5 4-2.5v-.4z"/></svg>sales@vornadrive.net</span>
  </div>
</div>
</body>
</html>
```